Voltline Assemblies, Inc. Business Card

Voltline has three operating entities and I'm looking for a standard business card template that can be used for Voltline and the three operating entities that the logo just get swapped out, but has a very similar look and feel. Ultimately if someone had a business card from each, they assume the organizations are related because they all have the same look and feel.
Below are our websites and I will attached the logos for each entity:
https://www.voltlineassemblies.example/
https://www.brantoceramic.example/
https://www.omra-kfsd.example/
https://www.summitbreaker.example/

Target Market(s)

US Voltline

Industry/Entity Type

US Voltline

Contact Information for Business Card

Normal stuff

```html
<!DOCTYPE html>
<html lang="en">
<head>
<meta charset="utf-8">
<title>Branto Ceramic Group Business Card</title>
<link rel="stylesheet" href="https://fonts.googleapis.com/css2?family=Roboto:wght@400&display=swap">
<style>
  :root {
    --backdrop: #c4c4c4;
    --card-black: #0e0e0f;
    --card-white: #ffffff;
    --brand-blue: #2d6fdc;
    --mark-silver: #dfe8f2;
    --ink: #1c1c1c;
    --icon-blue: #2f78e6;
    --radius: 26px;
  }
  * { margin: 0; padding: 0; box-sizing: border-box; }
  html, body {
    width: 1200px; height: 800px; overflow: hidden;
    background: var(--backdrop);
  }
  .sheet {
    width: 1200px; height: 800px;
    display: flex; flex-direction: column; align-items: center; justify-content: center;
    gap: 44px;
  }
  .card {
    position: relative;
    width: 590px; height: 337px;
    border-radius: var(--radius);
    overflow: hidden;
    background: var(--card-black);
    box-shadow: 0 10px 28px rgba(0,0,0,0.22);
  }

  /* Brand lockup: plain name beside a plain square */
  .lockup { display: flex; align-items: center; gap: 14px; }
  .lockup-square { background: var(--mark-silver); flex: none; }
  .lockup-text { display: flex; flex-direction: column; }
  .brand-name, .brand-tagline {
    font-family: "Roboto", Arial, sans-serif;
    font-weight: 400; color: var(--brand-blue);
    white-space: nowrap;
  }

  /* Front */
  .card-front { display: flex; align-items: center; justify-content: center; }
  .card-front .lockup-square { width: 70px; height: 70px; }
  .card-front .brand-name { font-size: 30px; line-height: 1.1; }
  .card-front .brand-tagline { font-size: 14px; margin-top: 6px; }

  /* Back */
  .card-back { background: var(--card-white); }
  .back-panel {
    position: absolute; left: 0; top: 0; bottom: 0; width: 262px;
    background: var(--card-black);
    display: flex; align-items: center; justify-content: center;
  }
  .back-edge { position: absolute; left: 262px; top: 0; height: 337px; width: 8px; }
  .card-back .lockup { gap: 9px; }
  .card-back .lockup-square { width: 40px; height: 40px; }
  .card-back .brand-name { font-size: 16px; line-height: 1.1; }
  .card-back .brand-tagline { font-size: 8px; margin-top: 3px; }

  .contact-list {
    position: absolute; left: 300px; top: 88px;
    list-style: none;
    font-family: "Roboto", Arial, sans-serif; color: var(--ink);
    display: flex; flex-direction: column; gap: 13px;
  }
  .contact-item { display: flex; align-items: center; gap: 12px; }
  .contact-icon { width: 22px; height: 22px; flex: none; }
  .contact-phone { font-size: 17px; }
  .contact-email { font-size: 13px; }
  .contact-address { font-size: 11.5px; line-height: 1.35; }
</style>
</head>
<body>
<main class="sheet">

  <section class="card card-front" aria-label="Card front">
    <div class="lockup">
      <div class="lockup-square"></div>
      <div class="lockup-text">
        <span class="brand-name">Branto Ceramic Group</span>
        <span class="brand-tagline">A Voltline Assemblies, Inc. Company</span>
      </div>
    </div>
  </section>

  <section class="card card-back" aria-label="Card back">
    <div class="back-panel">
      <div class="lockup">
        <div class="lockup-square"></div>
        <div class="lockup-text">
          <span class="brand-name">Branto Ceramic Group</span>
          <span class="brand-tagline">A Voltline Assemblies, Inc. Company</span>
        </div>
      </div>
    </div>
    <svg class="back-edge" viewBox="0 0 8 337" preserveAspectRatio="none" aria-hidden="true">
      <polygon fill="#0e0e0f" points="0,0 0,0 7,3 0,6 7,9 0,12 7,15 0,18 7,21 0,24 7,27 0,30 7,33 0,36 7,39 0,42 7,45 0,48 7,51 0,54 7,57 0,60 7,63 0,66 7,69 0,72 7,75 0,78 7,81 0,84 7,87 0,90 7,93 0,96 7,99 0,102 7,105 0,108 7,111 0,114 7,117 0,120 7,123 0,126 7,129 0,132 7,135 0,138 7,141 0,144 7,147 0,150 7,153 0,156 7,159 0,162 7,165 0,168 7,171 0,174 7,177 0,180 7,183 0,186 7,189 0,192 7,195 0,198 7,201 0,204 7,207 0,210 7,213 0,216 7,219 0,222 7,225 0,228 7,231 0,234 7,237 0,240 7,243 0,246 7,249 0,252 7,255 0,258 7,261 0,264 7,267 0,270 7,273 0,276 7,279 0,282 7,285 0,288 7,291 0,294 7,297 0,300 7,303 0,306 7,309 0,312 7,315 0,318 7,321 0,324 7,327 0,330 7,333 0,337"/>
    </svg>

    <ul class="contact-list">
      <li class="contact-item">
        <svg class="contact-icon" viewBox="0 0 24 24" aria-label="Phone">
          <circle cx="12" cy="12" r="12" fill="var(--icon-blue)"/>
          <path fill="#fff" d="M8.2 6.5l1.9-.3 1 2.6-1.2 1c.6 1.4 1.7 2.5 3.1 3.1l1-1.2 2.6 1-.3 1.9c-.1.6-.7 1-1.3.9C10.9 15 9 13.1 7.3 7.8c-.1-.6.3-1.2.9-1.3z"/>
        </svg>
        <span class="contact-phone">555-014-2700</span>
      </li>
      <li class="contact-item">
        <svg class="contact-icon" viewBox="0 0 24 24" aria-label="Fax">
          <circle cx="12" cy="12" r="12" fill="var(--icon-blue)"/>
          <rect x="8.5" y="6" width="7" height="3.5" fill="#fff"/>
          <rect x="6" y="10" width="12" height="5.5" rx="1" fill="#fff"/>
          <rect x="8.5" y="14" width="7" height="4" fill="#fff" stroke="var(--icon-blue)" stroke-width="1"/>
        </svg>
        <span class="contact-phone">555-014-2792</span>
      </li>
      <li class="contact-item">
        <svg class="contact-icon" viewBox="0 0 24 24" aria-label="Email">
          <circle cx="12" cy="12" r="12" fill="var(--icon-blue)"/>
          <rect x="6" y="8" width="12" height="8.5" rx="1" fill="#fff"/>
          <path d="M6.5 8.6l5.5 4.2 5.5-4.2" fill="none" stroke="var(--icon-blue)" stroke-width="1.2"/>
        </svg>
        <span class="contact-email">sales@brantoceramic.example</span>
      </li>
      <li class="contact-item">
        <svg class="contact-icon" viewBox="0 0 24 24" aria-label="Address">
          <circle cx="12" cy="12" r="12" fill="var(--icon-blue)"/>
          <path fill="#fff" d="M12 5.5a4.2 4.2 0 0 0-4.2 4.2c0 3.2 4.2 8.3 4.2 8.3s4.2-5.1 4.2-8.3A4.2 4.2 0 0 0 12 5.5z"/>
          <circle cx="12" cy="9.7" r="1.6" fill="var(--icon-blue)"/>
        </svg>
        <span class="contact-address">120 W. Market RT 9, Ste 2, PO Box 31;<br>Fairbrook OH, USA, 40012</span>
      </li>
    </ul>
  </section>

</main>
</body>
</html>
```